Stylish Business Cards Wanted

- DOUBLE SIDED Design Required -

High end, edgy cards for a corporate and personal stylist. Must include logo,
Name: Belinda Forsey
Title: Director and Stylist
telephone : +61 8 8217 4592
email: belinda@thegarbledger.example
website: thegarbledger.example
Tag: Corporate Workwear & Uniform Specialist | Personal Stylist
Would like nice icons for telephone, email, website

Target Market(s)

Businesses wanting stylish uniforms, people wanting stylish wardrobes

Industry/Entity Type

Corporate Workwear Stylist

Contact Information for Business Card

I would like black, white and gold foiling incorporated in the design - possibly a touch of the other colours on my branding guide attached Name: Belinda Forsey Title: Director and Stylist telephone : +61 8 8217 4592 email: belinda@thegarbledger.example website: thegarbledger.example Tag: Corporate Workwear & Uniform Specialist | Personal Stylist Would like nice icons for telephone, email, website

Font styles to use
Other font styles liked:
• Raleway

Colors

Designer to choose colors to be used in the design.

Requirements
Must have
• Gold foil accents

```html
<!DOCTYPE html>
<html lang="en">
<head>
<meta charset="utf-8">
<title>The Garb Ledger — Business Cards</title>
<link href="https://fonts.googleapis.com/css2?family=Open+Sans:wght@400;600&display=swap" rel="stylesheet">
<style>
  :root {
    --backdrop: #1c1c1c;
    --card: #141414;
    --gold: #c9b26a;
    --gold-light: #efe2a6;
    --gold-deep: #9c8440;
    --card-shadow: rgba(0, 0, 0, 0.55);
  }
  * { box-sizing: border-box; margin: 0; padding: 0; }
  html, body {
    width: 1200px;
    height: 900px;
    overflow: hidden;
    background: var(--backdrop);
    font-family: "Open Sans", Arial, sans-serif;
  }
  .stage {
    position: relative;
    width: 1200px;
    height: 900px;
    display: flex;
    flex-direction: column;
    align-items: center;
    justify-content: center;
    gap: 52px;
  }
  .card {
    position: relative;
    width: 620px;
    height: 354px;
    background: var(--card);
    box-shadow: 0 14px 30px var(--card-shadow);
    overflow: hidden;
  }
  .card__foil-edge {
    position: absolute;
    left: 0;
    right: 0;
    bottom: 0;
    height: 5px;
    background: linear-gradient(90deg, var(--gold-deep), var(--gold-light) 45%, var(--gold) 70%, var(--gold-deep));
  }

  /* Front */
  .front__wordmark {
    position: absolute;
    top: 92px;
    left: 0;
    right: 0;
    display: flex;
    justify-content: center;
    align-items: center;
    gap: 16px;
  }
  .front__mark {
    width: 18px;
    height: 18px;
    border-radius: 50%;
    background: var(--gold);
  }
  .front__name {
    font-size: 46px;
    font-weight: 600;
    color: var(--gold);
    letter-spacing: 1px;
  }
  .front__tagline {
    position: absolute;
    left: 0;
    right: 0;
    bottom: 52px;
    text-align: center;
    font-size: 15px;
    font-weight: 400;
    color: var(--gold);
    letter-spacing: 0.3px;
  }
  .front__tagline .dot { margin: 0 10px; }

  /* Back */
  .back__identity {
    position: absolute;
    top: 122px;
    right: 350px;
    text-align: right;
  }
  .back__person {
    font-size: 22px;
    font-weight: 600;
    color: var(--gold);
    text-transform: uppercase;
    letter-spacing: 0.5px;
  }
  .back__title {
    margin-top: 4px;
    font-size: 15px;
    color: var(--gold);
  }
  .back__divider {
    position: absolute;
    top: 112px;
    left: 290px;
    width: 1px;
    height: 96px;
    background: var(--gold-deep);
  }
  .back__contacts {
    position: absolute;
    top: 118px;
    left: 312px;
    list-style: none;
  }
  .contact {
    display: flex;
    align-items: center;
    gap: 9px;
    font-size: 15px;
    color: var(--gold);
    line-height: 28px;
  }
  .contact__icon { width: 13px; height: 13px; flex: none; }
</style>
</head>
<body>
<main class="stage">

  <section class="card card--front" aria-label="Card front">
    <div class="front__wordmark">
      <span class="front__mark"></span>
      <span class="front__name">The Garb Ledger</span>
    </div>
    <p class="front__tagline">Corporate Workwear &amp; Uniform Specialist<span class="dot">•</span>Personal Stylist</p>
    <div class="card__foil-edge"></div>
  </section>

  <section class="card card--back" aria-label="Card back">
    <div class="back__identity">
      <p class="back__person">Belinda Forsey</p>
      <p class="back__title">Director and Stylist</p>
    </div>
    <div class="back__divider"></div>
    <ul class="back__contacts">
      <li class="contact">
        <svg class="contact__icon" viewBox="0 0 16 16" aria-hidden="true">
          <path fill="#c9b26a" d="M3.6 1.2l2.3 2.6-1.3 1.7c.9 2 2.5 3.6 4.4 4.5l1.7-1.3 2.6 2.3-1.4 2.6C6.6 13.4 2.6 9.4 1 4.1z"/>
        </svg>
        +61 8 8217 4592
      </li>
      <li class="contact">
        <svg class="contact__icon" viewBox="0 0 16 16" aria-hidden="true">
          <rect x="1" y="3" width="14" height="10" fill="#c9b26a"/>
          <path d="M1 3.5l7 5 7-5" fill="none" stroke="#141414" stroke-width="1.3"/>
        </svg>
        belinda@thegarbledger.example
      </li>
      <li class="contact">
        <svg class="contact__icon" viewBox="0 0 16 16" aria-hidden="true">
          <circle cx="8" cy="8" r="6.5" fill="none" stroke="#c9b26a" stroke-width="1.5"/>
          <ellipse cx="8" cy="8" rx="2.8" ry="6.5" fill="none" stroke="#c9b26a" stroke-width="1.2"/>
          <path d="M1.5 8h13" stroke="#c9b26a" stroke-width="1.2"/>
        </svg>
        thegarbledger.example
      </li>
    </ul>
    <div class="card__foil-edge"></div>
  </section>

</main>
</body>
</html>
```